Hockey Sponsorship Proposal

We are looking for a sponsorship proposal design for an apparel company to supply our hockey camps with jerseys and apparel. We want to use lots of visuals so potential business partners can see the exposure and publicity their company could get by working with us. We would like the primary colors to be red, black and white. We have attached a bunch of images but not all need to be used. We would like to see a mix of images with adult players and youth players where appropriate. Although I have provided a rough outline for the information on the powerpoint the text and images can be displayed however you would like.

Here is a link to some proposals to give you an idea of what we are looking for
https://www.quillrack.co.uk/pin/512604837219056471/

Target Market(s)

Athletic Apparel Companies

Industry/Entity Type

It Company

Requirements
Must have
• Please note this should be suitable for web as the proposal will be emailed. This is NOT for print.
Nice to have
• I would like the first page to have a full image as the backdrop with the text over top if possible.

```html
<!DOCTYPE html>
<html lang="en">
<head>
<meta charset="utf-8">
<title>Hockey Sponsorship Proposal – About</title>
<link rel="stylesheet" href="https://fonts.googleapis.com/css2?family=Montserrat:wght@600;700&family=Barlow:wght@400;500&family=Arimo:wght@400;700&display=swap">
<style>
:root{
  --red:#e0373f;
  --red-deep:#9c2532;
  --black:#1f1f1f;
  --white:#ffffff;
  --paper:#f7f7f7;
  --ink:#2b2b2b;
  --link:#2a3fb5;
  --source:#2f8a3c;
  --backdrop:#e9e6e1;
}
*{box-sizing:border-box;margin:0;padding:0}
html,body{width:1200px;height:880px;overflow:hidden}
body{background:var(--backdrop);font-family:'Barlow',sans-serif;color:var(--ink);position:relative}
.spread{position:absolute;left:30px;top:262px;width:1140px;height:356px;display:flex;box-shadow:0 14px 30px rgba(0,0,0,.18)}
.page{position:relative;width:570px;height:356px;overflow:hidden}
.page--opportunity{background:var(--paper)}
.page--coach{background:linear-gradient(90deg,#dcdcdc 0,var(--white) 22px,var(--white) 100%)}
.rink-photo{position:absolute;inset:0 0 60px 0;background:linear-gradient(180deg,#9aa6ad 0%,#c8ccca 30%,#b44048 48%,#d9dde0 72%,#eef0f2 100%)}
.photo-fade{position:absolute;left:0;right:0;bottom:0;height:110px;background:linear-gradient(180deg,rgba(247,247,247,0) 0,rgba(247,247,247,.9) 45%,var(--paper) 100%)}
.banner{position:absolute;left:0;height:44px}
.page--opportunity .banner{top:18px;width:500px}
.page--coach .banner{top:22px;width:500px}
.banner-title{position:absolute;left:42px;top:0;line-height:44px;font-family:'Montserrat',sans-serif;font-weight:700;font-size:14px;letter-spacing:1.4px;color:var(--white);text-transform:uppercase}
.banner svg{position:absolute;inset:0}
.bullets{list-style:none;position:absolute}
.bullets li{position:relative;padding-left:10px;font-size:9.5px;line-height:12.5px}
.bullets li::before{content:"";position:absolute;left:0;top:5px;width:3.5px;height:3.5px;border-radius:50%;background:var(--ink)}
.page--opportunity .bullets{left:54px;bottom:36px;font-style:italic;letter-spacing:.2px}
.page--coach .bullets{left:40px;top:76px;width:480px}
.corner{position:absolute;bottom:0}
.corner--left{left:0}
.corner--right{right:0}
.media-heading{position:absolute;left:40px;top:136px;font-family:'Montserrat',sans-serif;font-weight:700;font-size:10px;letter-spacing:.9px;color:var(--red);text-transform:uppercase}
.media-grid{position:absolute;left:40px;top:156px;width:500px;display:grid;grid-template-columns:1fr 1fr;column-gap:26px;row-gap:10px}
.media-item{display:flex;gap:6px;font-family:'Arimo',sans-serif;font-size:5px;line-height:6.4px}
.media-thumb{flex:0 0 36px;height:32px;background:linear-gradient(135deg,#8b5a4a,#c9b8a6 55%,#e4e4e4)}
.media-title{color:var(--link)}
.media-title b,.media-snippet b{font-weight:700}
.media-source{color:var(--source)}
.media-snippet{color:#444}
.site-note{position:absolute;left:40px;bottom:42px;font-size:9.5px;letter-spacing:.2px}
.site-note a{color:var(--red);text-decoration:none}
</style>
</head>
<body>
<main class="spread">
  <section class="page page--opportunity">
    <div class="rink-photo" role="img" aria-label="Photo of players in red and white practice jerseys lined up on the ice with their coach at a hockey camp"></div>
    <div class="photo-fade"></div>
    <div class="banner">
      <svg viewBox="0 0 500 44" width="500" height="44" aria-hidden="true">
        <polygon points="0,0 500,0 500,44 0,44" fill="var(--red)" opacity=".92"/>
        <polygon points="380,0 470,0 438,44 348,44" fill="var(--red-deep)"/>
        <polygon points="452,0 500,0 500,0 500,44 420,44" fill="var(--black)"/>
      </svg>
      <h2 class="banner-title">About This Opportunity</h2>
    </div>
    <ul class="bullets">
      <li>Warren Halvorsen is seeking a partner to be his official jersey and apparel supplier.</li>
      <li>Selected supplier will outfit all participants of Warren’s NPL and youth hockey camps.</li>
      <li>Opportunity to outfit 50 NPL superstars and over 400 of North America’s top young hockey players.</li>
    </ul>
    <svg class="corner corner--left" width="110" height="16" viewBox="0 0 110 16" aria-hidden="true">
      <polygon points="0,0 26,0 34,16 0,16" fill="var(--black)"/>
      <polygon points="26,0 92,0 100,16 34,16" fill="var(--red-deep)"/>
    </svg>
  </section>

  <section class="page page--coach">
    <div class="banner">
      <svg viewBox="0 0 500 44" width="500" height="44" aria-hidden="true">
        <polygon points="0,4 440,4 440,40 0,40" fill="var(--red)"/>
        <polygon points="390,0 440,0 408,44 358,44" fill="var(--red-deep)"/>
        <polygon points="440,0 500,0 468,44 408,44" fill="var(--black)"/>
      </svg>
      <h2 class="banner-title">About Warren</h2>
    </div>
    <ul class="bullets">
      <li>Preeminent performance coach for many of the NPL’s biggest superstars including Cole Marchetti, Evan Rourke &amp; Liam Tessier.</li>
      <li>Player Development Consultant for the Lakeport Lynx.</li>
      <li>Regarded as an innovator and leading expert in uncovering new pathways of performance excellence.</li>
    </ul>

    <h3 class="media-heading">Warren in the Media</h3>
    <div class="media-grid">
      <article class="media-item">
        <div class="media-thumb" role="img" aria-label="News thumbnail of a player taking a shot"></div>
        <div>
          <p class="media-title">Lynx teammates break down Liam Tessier’s unique shooting ...</p>
          <p class="media-source">Rinkside.ca - Oct 19, 2017</p>
          <p class="media-snippet">According to Tessier’s father Brian, much of that unpredictable style can be credited to skills coach <b>Warren Halvorsen</b>, who’s worked with the ...</p>
        </div>
      </article>
      <article class="media-item">
        <div class="media-thumb" role="img" aria-label="News thumbnail of the coach at the rink"></div>
        <div>
          <p class="media-title">Lynx skills development coach <b>Warren Halvorsen</b> part of new philosophy</p>
          <p class="media-source">Lynx Den Blog - May 25, 2016</p>
          <p class="media-snippet">As the Lynx rebuild gets underway, the team’s newest skill development coach is just getting started. I had the chance to chat with <b>Warren Halvorsen</b> ...</p>
        </div>
      </article>
      <article class="media-item">
        <div class="media-thumb" role="img" aria-label="News thumbnail of two people in conversation"></div>
        <div>
          <p class="media-title">From Evan Rourke on down, <b>Warren Halvorsen</b> driven to develop players ...</p>
          <p class="media-source">The Blueline - May 9, 2017</p>
          <p class="media-snippet">Performance coach <b>Warren Halvorsen</b> is known best for the work he’s done with some of the NPL’s biggest stars of today. From Cole Marchetti to ...</p>
        </div>
      </article>
      <article class="media-item">
        <div class="media-thumb" role="img" aria-label="News thumbnail of players skating at a training session"></div>
        <div>
          <p class="media-title">NPL star players descend on Harbor Ice Center to train with Naples ...</p>
          <p class="media-source">The Coastal Ledger - Sep 4, 2017</p>
          <p class="media-snippet">For 25 years, <b>Warren Halvorsen</b> has been fascinated with the science of hockey. From replaying grainy tapes of ‘Saturday Night Hockey’ games to ...</p>
        </div>
      </article>
    </div>

    <p class="site-note">For more on Warren please visit <a href="#">halvorsenhockey.com</a></p>
    <svg class="corner corner--right" width="110" height="16" viewBox="0 0 110 16" aria-hidden="true">
      <polygon points="6,0 76,0 84,16 0,16" fill="var(--red-deep)"/>
      <polygon points="76,0 110,0 110,16 84,16" fill="var(--black)"/>
    </svg>
  </section>
</main>
</body>
</html>
```